Trendora - Forex Signal Services Moment is All. Shape your path.

I need an attractive eye catching web design that is azure friendly. I currently have a web programmer working on the backend of my website. Now I need a professional design to attract and retain customers. This site needs to be mobile friendly.

Trendora is a highly reputable, trustworthy and professional site that offers forex signals to traders in all parts of the globe. With accurate and reliable forex signals, traders can not only make money but also boost their profits.

At Trendora, we want our clients to have complete faith on us and our services! We also do not want our users to lead a simple and monotonous life. Instead our goal is to help them create an extra source of steady income. However, this is possible only when our clients resolve to change their lives for the better. They need to change their mindset and most importantly develop a positive frame of mind. That’s exactly why at Trendora, we provide our clients with innumerable personal development tools and resources that’ll aid them in changing all the aspects of their lives. We want our traders to feel inspired and educate them in the right way!

Colors are flexible.

I do like the simplicity of www.bluemarrowtrade.example.
I do want a design more professional in appearance and not everything on page one.

I have not been able to decide on a logo. There is one of lower quality as I have not paid for it yet but I will if you decide it's the best for my business I will. Or should one feel that they have a better idea for a logo, I will pay for it if i like it.

I have included some of the content of my site so you can get a feel for where I am coming from.
(Please note that this content is still in the editing process)

Project Deadline Extended Reason: My content was not complete nor finalization of the final logo. We will allow a few more days for designers to modify the website.Thank you for your patience and understanding. Added Tuesday, January 24, 2017

Target Market(s)

I work with Forex Traders, Investors wanting to control their own portfolios, and remote nomads/mellienials

Coding

Coded - Design and coding required

Number of Pages Required

5+ page

Requirements
Must have
• I must have a professional clean look. I want the site to be interactive and eye catching. I want my audience hooked within seconds of opening it. It has to have all important information first. Photos must be legit and not spammy. I work as a representative in the financial market. I want my site to reflect that I stand by my product and reputation means everything to me. This site has to be engaging.
• Sorry, I should have included this earlier of what I will all need on this site.
• I'll have about Trendora (my company, what we stand for, who we work with, my strategy, etc....
• about me (why i started this company, who I am)
• Performance (graphs and recent posts of signals)
• Membership (how to sign up)
• Terms of service/legal/disclaimers
• FAQS
• Personal Development Resources
• Forex Education Resources
Nice to have
• Quick links to bounce around the site faster.
Should not have
• I do not want over the top white collar conservative.

```html
<!DOCTYPE html>
<html lang="en">
<head>
<meta charset="utf-8">
<title>Trendora - Forex Signal Services</title>
<link rel="stylesheet" href="https://fonts.googleapis.com/css2?family=Montserrat:wght@400;600;700&family=Open+Sans:wght@400;600&display=swap">
<style>
:root{
  --navy:#1d2935;
  --navy-deep:#15202a;
  --green:#6f8f4a;
  --green-soft:#8fa87a;
  --green-photo:#7d9468;
  --green-dark:#4e6a3a;
  --paper:#f3f5f1;
  --ink:#3a3f44;
  --muted:#6d747a;
  --white:#ffffff;
  --line:#d7ddd2;
}
*{box-sizing:border-box;margin:0;padding:0}
html,body{width:1200px;height:2536px;overflow:hidden}
body{font-family:"Open Sans",sans-serif;color:var(--ink);background:var(--white)}
h1,h2,h3,.nav,.btn,.price{font-family:"Montserrat",sans-serif}

.site-header{position:absolute;top:0;left:0;width:1200px;height:44px;background:var(--navy);display:flex;align-items:center;padding:0 40px;justify-content:space-between}
.brand{display:flex;align-items:center;gap:8px;color:var(--white);font-family:"Montserrat",sans-serif;font-weight:600;font-size:18px}
.brand-dot{width:12px;height:12px;background:var(--green-soft)}
.nav{display:flex;gap:26px;font-size:10px;font-weight:600;color:#c9d1d8;letter-spacing:.5px}
.nav .active{color:var(--white)}

.hero{position:absolute;top:44px;left:0;width:1200px;height:556px;background:linear-gradient(120deg,#97ab84 0%,var(--green-photo) 45%,#6c8259 100%);text-align:center;color:var(--white)}
.hero-photo{position:absolute;inset:0;background:linear-gradient(90deg,rgba(60,80,50,.25),rgba(255,255,255,.08) 50%,rgba(60,80,50,.25))}
.hero-content{position:absolute;top:230px;left:0;width:100%}
.hero h1{font-size:44px;font-weight:700;letter-spacing:4px}
.hero p{width:520px;margin:14px auto 0;font-size:13px;line-height:1.6}
.arrow{position:absolute;top:290px;width:30px;height:44px;background:rgba(40,50,40,.55);display:flex;align-items:center;justify-content:center}
.arrow.left{left:0}.arrow.right{right:0}

.welcome{position:absolute;top:600px;left:0;width:1200px;height:520px;background:var(--paper);text-align:center;padding:60px 140px 0}
.welcome h2{font-size:34px;font-weight:600;color:var(--navy)}
.tagline{margin-top:14px;font-family:"Montserrat",sans-serif;font-size:17px;font-weight:600;color:var(--navy);letter-spacing:1px}
.sub{margin-top:8px;font-family:"Montserrat",sans-serif;font-size:13px;font-weight:600;color:var(--green);letter-spacing:2px}
.welcome p{margin-top:18px;font-size:13px;line-height:1.75;color:var(--muted)}
.welcome h3{margin-top:26px;font-size:14px;color:var(--green);letter-spacing:1px}

.membership{position:absolute;top:1120px;left:0;width:1200px;height:450px;background:linear-gradient(110deg,#8aa276,var(--green-photo) 50%,#94aa80);text-align:center;color:var(--white);padding:60px 160px 0}
.membership h2{font-size:34px;font-weight:400;letter-spacing:1px}
.membership p{margin-top:18px;font-size:13px;line-height:1.7}
.price{margin-top:26px;font-size:18px;font-weight:600}
.term{font-family:"Montserrat",sans-serif;font-size:30px;font-weight:700;margin-top:2px}
.btn{display:inline-block;margin-top:18px;background:var(--navy);color:var(--white);font-size:13px;font-weight:600;padding:12px 30px;letter-spacing:1px}

.faq{position:absolute;top:1570px;left:0;width:1200px;height:440px;background:#e9ede5}
.faq-photo{position:absolute;left:0;top:0;width:240px;height:440px;background:linear-gradient(180deg,#c9d3bf,#aebd9f)}
.faq h2{position:absolute;top:30px;width:100%;text-align:center;font-size:34px;color:var(--navy);letter-spacing:3px}
.faq-col{position:absolute;top:100px}
.faq-col.left{left:240px;width:380px}
.faq-col.right{left:650px;width:390px}
.q{display:flex;align-items:center;gap:10px;background:var(--white);border:1px solid var(--line);padding:9px 12px;font-size:11px;font-weight:600;color:var(--navy);margin-bottom:10px}
.q-icon{width:14px;height:14px;background:var(--green);flex:none}
.answer{background:var(--white);border:1px solid var(--line);border-top:none;margin-top:-10px;margin-bottom:10px;padding:12px;font-size:10.5px;line-height:1.65;color:var(--muted)}

.contact{position:absolute;top:2010px;left:0;width:1200px;height:430px;background:var(--navy);color:var(--white)}
.contact h2{position:absolute;top:30px;width:100%;text-align:center;font-size:30px;font-weight:600;letter-spacing:3px}
.contact-info{position:absolute;top:110px;left:130px;width:300px}
.contact-info p{font-size:12px;line-height:1.6;color:#c3ccd4}
.phone-row{display:flex;align-items:center;gap:10px;margin-top:16px}
.phone{font-family:"Montserrat",sans-serif;font-size:26px;font-weight:700}
.stay{margin-top:26px;font-family:"Montserrat",sans-serif;font-size:14px;font-weight:600;letter-spacing:2px}
.socials{display:flex;gap:10px;margin-top:12px}
.socials span{width:32px;height:32px;border-radius:50%;background:var(--green-soft)}
.contact-form{position:absolute;top:110px;left:470px;width:600px;display:grid;grid-template-columns:1fr 1fr;gap:12px}
.field{height:34px;background:var(--navy-deep);border:1px solid #3a4a59;font-size:11px;color:#9aa6b1;padding:9px 12px}
.field.wide{grid-column:1/3;height:110px}
.newsletter{position:absolute;top:370px;left:130px;width:940px;display:flex;align-items:center;gap:12px}
.newsletter .field{flex:1}
.newsletter .label{font-size:12px;color:#c3ccd4;width:180px}
.btn.send{margin:0;padding:10px 26px;background:var(--green);font-size:12px}

.site-footer{position:absolute;top:2440px;left:0;width:1200px;height:96px;background:var(--navy-deep);color:#9aa6b1;padding:22px 130px;display:flex;justify-content:space-between;font-size:10px}
.footer-links{display:flex;gap:30px;font-family:"Montserrat",sans-serif;font-weight:600;color:#c9d1d8}
.footer-links div{line-height:1.8}
.legal{line-height:1.7}
</style>
</head>
<body>

<header class="site-header">
  <div class="brand"><span class="brand-dot"></span>Trendora</div>
  <nav class="nav">
    <span class="active">HOME</span><span>ABOUT US</span><span>MEMBERSHIP PLANS</span><span>PERFORMANCE</span><span>FAQ</span><span>FOREX EDUCATION</span><span>CONTACT US</span>
  </nav>
</header>

<section class="hero">
  <div class="hero-photo" role="img" aria-label="Trader holding a smartphone showing forex charts, green toned"></div>
  <div class="arrow left"><svg width="10" height="16"><path d="M8 2 2 8l6 6" stroke="#fff" stroke-width="2" fill="none"/></svg></div>
  <div class="arrow right"><svg width="10" height="16"><path d="m2 2 6 6-6 6" stroke="#fff" stroke-width="2" fill="none"/></svg></div>
  <div class="hero-content">
    <h1>FOREX SIGNAL</h1>
    <p>Signals you can trust, built on tested strategy and delivered daily to traders in every time zone across the globe.</p>
  </div>
</section>

<section class="welcome">
  <h2>Welcome to Trendora</h2>
  <div class="tagline">MOMENT IS ALL.&nbsp; SHAPE YOUR PATH.</div>
  <div class="sub">FOREX SIGNAL SERVICES</div>
  <p>We provide accurate forex signals to traders in every part of the globe, backed by a disciplined strategy and clear risk rules. Our aim is to help each member build a steady extra income while growing as a confident, independent trader.</p>
  <p>Alongside our signals we share personal development tools and learning resources that support the right mindset. We want every trader to feel inspired, stay focused and understand the reasoning behind each trade we send.</p>
  <h3>WHAT IS YOUR TRADING PHILOSOPHY AND STYLE?</h3>
  <p>We follow price action on the higher time frames, combining key levels with patient entries and strict stop placement. Every signal includes entry, stop loss and take profit so you always know the plan before the market moves.</p>
</section>

<section class="membership" role="img" aria-label="Green toned background photo of a trading desk">
  <h2>Membership Plans</h2>
  <p>Choose a plan that fits your trading goals. Every membership includes daily signals, weekly market outlooks, member chat access and our full library of education and personal development resources.</p>
  <p>Cancel anytime from your dashboard. No hidden fees and no long contracts.</p>
  <div class="price">$ 58 USD</div>
  <div class="term">1 MONTH</div>
  <span class="btn">SIGN UP NOW</span>
</section>

<section class="faq">
  <div class="faq-photo" role="img" aria-label="Hand holding a phone with a trading app"></div>
  <h2>FAQ</h2>
  <div class="faq-col left">
    <div class="q"><span class="q-icon"></span>How do I receive my signals after joining?</div>
    <div class="answer">Once your membership is active you will receive each signal by email and in the members area within seconds of it being posted. Every alert lists the currency pair, direction, entry price, stop loss and take profit levels. You can also turn on mobile notifications so you never miss a trade, even while travelling. Our team posts a short note with each setup explaining the reasoning, and we follow up when a trade is closed or adjusted. If you ever have a question about a signal, our support desk replies within one business day.</div>
    <div class="q"><span class="q-icon"></span>Can I follow your signals on any broker?</div>
    <div class="q"><span class="q-icon"></span>Do I need trading experience?</div>
    <div class="q"><span class="q-icon"></span>What happens after my trial ends?</div>
  </div>
  <div class="faq-col right">
    <div class="q"><span class="q-icon"></span>How accurate are your signals?</div>
    <div class="q"><span class="q-icon"></span>What time are signals sent each day?</div>
    <div class="q"><span class="q-icon"></span>Which currency pairs do you cover?</div>
    <div class="q"><span class="q-icon"></span>How much capital should I start with?</div>
    <div class="q"><span class="q-icon"></span>Can I cancel my membership at any time?</div>
    <div class="q"><span class="q-icon"></span>Do you offer refunds on plans?</div>
  </div>
</section>

<section class="contact">
  <h2>CONTACT US</h2>
  <div class="contact-info">
    <p>If you would like to get in touch with our team, fill out the form or give us a call. We answer every message.</p>
    <div class="phone-row">
      <svg width="22" height="22" viewBox="0 0 24 24"><path d="M6.6 10.8a15 15 0 0 0 6.6 6.6l2.2-2.2a1 1 0 0 1 1-.25 11.4 11.4 0 0 0 3.6.57 1 1 0 0 1 1 1V20a1 1 0 0 1-1 1A17 17 0 0 1 3 4a1 1 0 0 1 1-1h3.5a1 1 0 0 1 1 1c0 1.25.2 2.45.57 3.57a1 1 0 0 1-.25 1z" fill="#8fa87a"/></svg>
      <span class="phone">0800 555 0147</span>
    </div>
    <div class="stay">STAY CONNECTED</div>
    <div class="socials"><span></span><span></span><span></span><span></span></div>
  </div>
  <div class="contact-form">
    <div class="field">Name</div>
    <div class="field">Email</div>
    <div class="field">Phone</div>
    <div class="field">Subject</div>
    <div class="field wide">Message</div>
  </div>
  <div class="newsletter">
    <span class="label">Sign up for our newsletter</span>
    <div class="field">Email</div>
    <span class="btn send">Send</span>
  </div>
</section>

<footer class="site-footer">
  <div class="legal">© 2017 Trendora. All rights reserved.<br>Forex trading involves risk. Trade responsibly.</div>
  <div class="footer-links">
    <div>HOME<br>ABOUT US</div>
    <div>MEMBERSHIP<br>PERFORMANCE</div>
    <div>FAQ<br>EDUCATION</div>
    <div>CONTACT US<br>Follow us</div>
  </div>
</footer>

</body>
</html>
```